Signage Design Project - Florida Vacation Resort Monument Sign

I need a design for the main identification sign outside of a resort in Florida. This is a sign that will be located at ground level near the entrance to the resort.

Text to include:

"5817" (This is the property address numbers, no street name necessary)

"Coral Haven" (This is the name of the resort)

"Heated Pool" (bullet point)
"Tiki Hut" (bullet point)
"Beach Access" (bullet point)

"Weekly/Monthly Rentals" (text to appear at bottom of sign)

Dimensions: 55.5"wide x 43.5"tall

Some design elements can protrude from the dimensions, as long as they are not too thin. It will ultimately need to be cut out of wood and if a design element is thin and sticks out of the box, it will be likely to break off.

***The artwork must be vectored.***

Please use whatever design elements you'd like in full color. A palm tree might make sense because of the name "Coral Haven", but I don't want to limit your creativity!

The website is here: http://www.coral-haven-example.com

They have a tour your can click on at the bottom for more pictures to get a feel for the property.

```html
<!DOCTYPE html>
<html lang="en">
<head>
<meta charset="utf-8">
<title>Coral Haven Monument Sign</title>
<link rel="stylesheet" href="https://fonts.googleapis.com/css2?family=Arimo:wght@700&family=Tinos&family=Fredoka:wght@500&display=swap">
<style>
  :root {
    --bg: #ffffff;
    --parchment-center: #fffaf0;
    --parchment-mid: #fde2bc;
    --parchment-edge: #f4c088;
    --bamboo: #d9a257;
    --bamboo-dark: #b07a3c;
    --ink: #111111;
    --title-green: #1f6b22;
    --footer-green: #1d4f1d;
  }
  html, body {
    margin: 0;
    padding: 0;
    overflow: hidden;
    background: var(--bg);
  }
  .sign {
    position: relative;
    width: 1200px;
    height: 917px;
    overflow: hidden;
    background: var(--bg);
  }
  .sign-artwork {
    position: absolute;
    inset: 0;
    border-radius: 28px;
    background: radial-gradient(ellipse 58% 58% at 50% 50%,
      var(--parchment-center) 0%,
      var(--parchment-mid) 55%,
      var(--parchment-edge) 82%,
      var(--bamboo) 94%,
      var(--bamboo-dark) 100%);
  }
  .address-number {
    position: absolute;
    top: 121px;
    left: 0;
    width: 1200px;
    margin: 0;
    text-align: center;
    font: 700 76px/1 "Arimo", Arial, sans-serif;
    color: var(--ink);
  }
  .resort-name {
    position: absolute;
    top: 276px;
    left: 0;
    width: 1200px;
    margin: 0;
    text-align: center;
    font: 400 140px/1 "Tinos", "Times New Roman", serif;
    color: var(--title-green);
    letter-spacing: 1px;
  }
  .amenities {
    position: absolute;
    top: 480px;
    left: 362px;
    margin: 0;
    padding: 0;
    list-style: none;
    font: 700 72px/78px "Arimo", Arial, sans-serif;
    color: var(--ink);
  }
  .amenities li::before {
    content: "\2022";
    display: inline-block;
    width: 54px;
  }
  .rental-terms {
    position: absolute;
    top: 740px;
    left: 0;
    width: 1200px;
    margin: 0;
    text-align: center;
    font: 500 66px/1 "Fredoka", "Trebuchet MS", sans-serif;
    color: var(--footer-green);
  }
</style>
</head>
<body>
<main class="sign">
  <div class="sign-artwork" role="img" aria-label="Torn parchment panel inside a lashed bamboo frame, with palm trees at the bottom left and right corners"></div>
  <p class="address-number">5817</p>
  <h1 class="resort-name">Coral Haven</h1>
  <ul class="amenities">
    <li>Heated Pool</li>
    <li>Tiki Hut</li>
    <li>Beach Access</li>
  </ul>
  <p class="rental-terms">Weekly/Monthly Rentals</p>
</main>
</body>
</html>
```